Teachers workshop flyer

I need a flyer to inform schools of a workshop for teachers that empowers the teacher to help traumatised and disadvantaged students to engage in successful learning.

I am a teacher and educator and my info for the flyer is attached.

Target Market(s)

Principals and vice-principals who have stressed staff and students and they want things to be better in the school!

Industry/Entity Type

Teacher

```html
<!DOCTYPE html>
<html lang="en">
<head>
<meta charset="utf-8">
<title>Brain-Based Strategies for Student Success</title>
<link rel="stylesheet" href="https://fonts.googleapis.com/css2?family=EB+Garamond:wght@700;800&family=Arimo:wght@400;700&display=swap">
<style>
  :root {
    --page-bg: #e9e6e1;
    --cream: #f3e5cc;
    --brown: #3b2415;
    --footer-brown: #3a2416;
    --ink: #2f2620;
    --green: #8cc63f;
    --white: #ffffff;
  }
  * { box-sizing: border-box; margin: 0; padding: 0; }
  html, body { width: 1200px; height: 960px; overflow: hidden; background: var(--page-bg); }
  .flyer {
    position: absolute; left: 20px; top: 69px; width: 1160px; height: 822px;
    background: var(--white); overflow: hidden;
    box-shadow: 0 4px 18px rgba(0,0,0,0.15);
    font-family: "Arimo", Arial, sans-serif; color: var(--ink);
  }
  .intro-panel { position: absolute; left: 0; top: 0; width: 701px; height: 491px; background: var(--cream); }
  .title {
    position: absolute; left: 51px; top: 40px;
    font-family: "EB Garamond", Garamond, serif; font-weight: 700; color: var(--brown);
    line-height: 1; letter-spacing: 0.5px;
  }
  .title span { display: block; }
  .title .line-1 { font-size: 84px; }
  .title .line-2 { font-size: 64px; margin-top: 2px; }
  .title .line-3 { font-size: 60px; margin-top: 4px; }
  .intro-text {
    position: absolute; left: 51px; width: 601px;
    font-size: 15.5px; line-height: 22.4px; text-align: justify;
  }
  .intro-text.first { top: 264px; }
  .intro-text.second { top: 382px; }
  .photo { position: absolute; left: 701px; width: 459px; }
  .photo.students { top: 0; height: 248px; background: linear-gradient(135deg, #c9b7a2 0%, #e9b69a 35%, #d8566e 60%, #5d86c4 100%); }
  .photo.teachers { top: 248px; height: 243px; background: radial-gradient(ellipse at 50% 60%, #e4d6c4 0%, #f2ece4 55%, #ffffff 85%); }
  .accent-bar { position: absolute; left: 0; top: 491px; width: 1160px; height: 9px; background: var(--green); }
  .section-heading { position: absolute; font-size: 19.5px; font-weight: 700; color: var(--brown); }
  .about-heading { left: 51px; top: 520px; }
  .feedback-heading { left: 575px; top: 524px; }
  .about-text {
    position: absolute; left: 51px; top: 553px; width: 455px;
    font-size: 15.6px; line-height: 24.7px; text-align: justify; letter-spacing: 0.2px;
  }
  .about-text .presenter-name { font-weight: 700; font-size: 18px; color: var(--brown); }
  .divider { position: absolute; left: 550px; top: 522px; width: 3px; height: 204px; }
  .testimonial { position: absolute; left: 602px; width: 515px; font-size: 14.7px; line-height: 19.6px; }
  .testimonial.one { top: 570px; text-align: justify; }
  .testimonial.two { top: 650px; }
  .quote-mark {
    position: absolute; font-family: "EB Garamond", Georgia, serif; font-weight: 800;
    font-size: 46px; line-height: 1; color: var(--brown);
  }
  .quote-mark.open-one { left: 576px; top: 560px; }
  .quote-mark.close-one { left: 968px; top: 610px; }
  .quote-mark.open-two { left: 576px; top: 640px; }
  .quote-mark.close-two { left: 942px; top: 711px; }
  .footer {
    position: absolute; left: 0; top: 740px; width: 1160px; height: 82px; background: var(--footer-brown);
    color: var(--white); text-align: center; font-size: 23.5px; line-height: 28px;
    letter-spacing: 1.2px; padding-top: 12px;
  }
  .footer strong { font-weight: 700; }
</style>
</head>
<body>
<main class="flyer">
  <section class="intro-panel">
    <h1 class="title">
      <span class="line-1">BRAIN-BASED</span>
      <span class="line-2">STRATEGIES FOR</span>
      <span class="line-3">STUDENT SUCCESS</span>
    </h1>
    <p class="intro-text first">Contemporary teaching is a highly complex role as increasing numbers of students attend school without the essential ‘self-skills’ to be truly ‘school-ready’ and successful. Instead these students often seek-out attention in ways that can disruptive in the classroom causing stress and frustration for teachers.</p>
    <p class="intro-text second">Dan shows how and why the most effective strategies for these students are guided by a sound understanding of child-development and brain-development - especially where trauma has left lasting impacts. Teachers can learn how to build a student’s self-skills, without the teacher having to become a therapist!</p>
  </section>

  <div class="photo students" role="img" aria-label="Photo of a smiling group of students giving thumbs up"></div>
  <div class="photo teachers" role="img" aria-label="Photo of a group of smiling teachers in light suits giving thumbs up"></div>

  <div class="accent-bar"></div>

  <h2 class="section-heading about-heading">About the Presenter:</h2>
  <p class="about-text"><span class="presenter-name">Daniel Whitfield</span> is a Melbourne-based therapist and educator with over twenty years experience working with adults and young people in the area of trauma and recovery. Dan’s seminars are engaging and practical since teachers need effective strategies that will immediately translate into classroom practice. Dan has trained here and overseas in the most effective behavior change strategies.</p>

  <svg class="divider" width="3" height="204" viewBox="0 0 3 204" aria-hidden="true">
    <defs>
      <linearGradient id="divider-fade" x1="0" y1="0" x2="0" y2="1">
        <stop offset="0" stop-color="#8cc63f" stop-opacity="0.9"/>
        <stop offset="0.5" stop-color="#8cc63f" stop-opacity="0.25"/>
        <stop offset="1" stop-color="#8cc63f" stop-opacity="0.9"/>
      </linearGradient>
    </defs>
    <rect width="3" height="204" fill="url(#divider-fade)"/>
  </svg>

  <h2 class="section-heading feedback-heading">Teacher Feedback:</h2>
  <span class="quote-mark open-one">“</span>
  <p class="testimonial one">Dan was such an engaging and energetic presenter whom I enjoyed immensely. His presentation on the brain and take away strategies were so practical and meaningful. It was an invaluable session.</p>
  <span class="quote-mark close-one">”</span>

  <span class="quote-mark open-two">“</span>
  <p class="testimonial two">My Light-bulb moments:<br>- I need to CONNECT – not correct – far more often.<br>- Seeing negative self-talk for what it is.<br>- Using far more ‘diversions’ in the avoidance loop.</p>
  <span class="quote-mark close-two">”</span>

  <footer class="footer">
    Call: <strong>0400 123 456</strong> for more information or to book Dan to come to your<br>
    school: www.<strong>danielwhitfield</strong>.com.au/studentsuccess
  </footer>
</main>
</body>
</html>
```